Redesign the *Settings* screen for the BrelloZ app.

BrelloZ app is in production, but we need to refresh and redesign the settings screen to be cleaner, easier, more intuitive, and more professional looking.

Project Deadline Extended
Reason: Several designers have requested more time. This will also give time to provide feedback on existing designs.

Requirements
Must have
• Black background, so that the screen is consistent with the rest of the app.

```html
<!DOCTYPE html>
<html lang="en">
<head>
<meta charset="utf-8">
<title>BrelloZ – Settings</title>
<link rel="stylesheet" href="https://fonts.googleapis.com/css2?family=Roboto:wght@400;500;700&display=swap">
<style>
  :root{
    --board:#e8eaed;
    --screen:#1b2027;
    --status:#161a20;
    --header-dark:#212a31;
    --teal:#1fc6ae;
    --teal-deep:#17a893;
    --text:#e9edf0;
    --muted:#7d8791;
    --line:#2c343d;
    --tabbar:#171b21;
  }
  *{box-sizing:border-box;margin:0;padding:0}
  html,body{width:900px;height:1200px;overflow:hidden;background:var(--board)}
  body{font-family:"Roboto",Arial,sans-serif;color:var(--text)}
  .board{position:relative;width:900px;height:1200px;background:var(--board);overflow:hidden}
  .screen{position:absolute;top:15px;width:384px;height:879px;background:var(--screen);overflow:hidden;box-shadow:0 2px 10px rgba(0,0,0,.18)}
  .screen--dark-header{left:60px}
  .screen--teal-header{left:456px}

  .status-bar{position:absolute;top:0;left:0;right:0;height:18px;background:var(--status);display:flex;align-items:center;justify-content:space-between;padding:0 8px;font-size:8px;color:#cfd5da}
  .status-bar .time{position:absolute;left:0;right:0;text-align:center}
  .app-header{position:absolute;top:18px;left:0;right:0;height:39px;display:flex;align-items:center;justify-content:center;font-size:13px;font-weight:500}
  .screen--dark-header .app-header{background:var(--header-dark);color:var(--teal)}
  .screen--teal-header .app-header{background:var(--teal);color:#fff}
  .app-header .back{position:absolute;left:14px;top:12px}

  .row{position:absolute;left:18px;right:18px;height:36px;margin-top:-18px;display:flex;align-items:center;justify-content:space-between;font-size:12px}
  .row-label{font-size:12px;color:var(--text)}
  .value{color:var(--teal);font-weight:500;font-size:11px}
  .icon-pair{display:flex;gap:10px;align-items:center}
  .icon-circle{width:30px;height:30px;border-radius:50%;border:1px solid var(--muted);display:flex;align-items:center;justify-content:center}
  .icon-circle--active{border-color:var(--teal);background:var(--teal)}
  .icon-plain{width:30px;height:30px;display:flex;align-items:center;justify-content:center}
  .info{width:13px;height:13px;border-radius:50%;border:1px solid var(--text);font-size:8px;display:flex;align-items:center;justify-content:center;font-weight:700}

  .seg{position:absolute;left:18px;right:18px;height:24px;margin-top:-12px;border:1px solid var(--teal);border-radius:12px;display:flex;overflow:hidden;font-size:9px}
  .seg span{flex:1;display:flex;align-items:center;justify-content:center;color:var(--text)}
  .seg .is-selected{background:var(--teal);color:#10201d;font-weight:500;border-radius:11px}

  .action{position:absolute;left:18px;right:18px;height:30px;margin-top:-15px;display:flex;align-items:center;gap:10px;font-size:11px;letter-spacing:.3px;text-transform:uppercase}
  .logout{position:absolute;left:142px;width:100px;top:723px;height:30px;border-radius:15px;background:var(--teal);color:#fff;font-size:10px;font-weight:500;display:flex;align-items:center;justify-content:center;letter-spacing:.5px}
  .sync-info{position:absolute;left:18px;right:18px;top:795px;display:flex;justify-content:space-between;font-size:8px;color:#c9d0d6}

  .tab-bar{position:absolute;left:0;right:0;bottom:0;height:40px;background:var(--tabbar);border-top:1px solid var(--line);display:flex}
  .tab{flex:1;display:flex;flex-direction:column;align-items:center;justify-content:center;gap:3px;font-size:7px;color:var(--muted);letter-spacing:.4px}
  .tab--active{color:var(--teal);background:#1f272e}
</style>
</head>
<body>
<div class="board">

  <section class="screen screen--dark-header" aria-label="Settings screen, dark header">
    <div class="status-bar"><span>●●●○○ NetCo</span><span class="time">12:45 AM</span><span>100%</span></div>
    <header class="app-header">
      <svg class="back" width="14" height="14" viewBox="0 0 14 14"><path d="M13 7H2M6 2L1 7l5 5" stroke="currentColor" stroke-width="1.6" fill="none"/></svg>
      Settings
    </header>

    <div class="row" style="top:84px"><span class="row-label">Pistol</span>
      <div class="icon-pair">
        <span class="icon-circle icon-circle--active"><svg width="16" height="14" viewBox="0 0 16 14"><path d="M1 2h14v4H8l-1 2H5l-1 5H1l1-6H1z" fill="#fff"/></svg></span>
        <span class="icon-plain"><svg width="16" height="16" viewBox="0 0 16 16"><path d="M2 14l10-10 2 2-10 10H2z" stroke="#c9d0d6" stroke-width="1.3" fill="none"/></svg></span>
      </div></div>
    <div class="row" style="top:126px"><span class="row-label">Current Firearm</span><span class="value">R400</span></div>
    <div class="row" style="top:168px"><span class="row-label">Right Handed</span>
      <div class="icon-pair">
        <span class="icon-plain"><svg width="14" height="16" viewBox="0 0 14 16"><path d="M3 15V6M6 15V2M9 15V3M12 15V6" stroke="#7d8791" stroke-width="1.6" stroke-linecap="round"/></svg></span>
        <span class="icon-circle icon-circle--active"><svg width="14" height="16" viewBox="0 0 14 16"><path d="M3 15V6M6 15V2M9 15V3M12 15V6" stroke="#fff" stroke-width="1.6" stroke-linecap="round"/></svg></span>
      </div></div>
    <div class="row" style="top:210px"><span class="row-label">Dry Practice</span>
      <div class="icon-pair">
        <span class="icon-circle"><svg width="10" height="16" viewBox="0 0 10 16"><rect x="1" y="1" width="8" height="14" rx="4" stroke="#c9d0d6" fill="none"/></svg></span>
        <span class="icon-plain value" style="color:#4b545d;font-size:9px">DRY</span>
      </div></div>

    <div class="row" style="top:252px"><span class="row-label">Device Mount Position</span><span class="info">i</span></div>
    <div class="seg" style="top:291px"><span>Forwards</span><span class="is-selected">Backwards</span></div>
    <div class="row" style="top:345px"><span class="row-label">Device Mount Location</span><span class="info">i</span></div>
    <div class="seg" style="top:381px"><span class="is-selected">Bottom</span><span>Top</span><span>Left</span><span>Right</span></div>
    <div class="row" style="top:441px"><span class="row-label">Bullseye Mode</span><span class="info">i</span></div>
    <div class="seg" style="top:480px"><span>Off</span><span class="is-selected">On</span></div>

    <div class="action" style="top:552px"><svg width="12" height="12" viewBox="0 0 12 12"><path d="M10 4A4.5 4.5 0 0 0 2 5M2 8a4.5 4.5 0 0 0 8-1M10 1v3H7M2 11V8h3" stroke="#e9edf0" stroke-width="1.2" fill="none"/></svg>Sync Account Data</div>
    <div class="action" style="top:597px"><svg width="12" height="12" viewBox="0 0 12 12"><path d="M3 3l6 6-3 2V1l3 2-6 6" stroke="#e9edf0" stroke-width="1.2" fill="none"/></svg>Disconnect Bluetooth</div>
    <div class="action" style="top:642px"><svg width="12" height="12" viewBox="0 0 12 12"><path d="M2 11V1h8l-2 3 2 3H2" stroke="#e9edf0" stroke-width="1.2" fill="none"/></svg>Report Issue</div>

    <div class="logout">LOGOUT</div>
    <div class="sync-info"><span>Last synced: 8:56am monday 21st 2017</span><span>v2.3.0.85</span></div>

    <nav class="tab-bar">
      <div class="tab"><svg width="12" height="12" viewBox="0 0 12 12"><circle cx="6" cy="6" r="5" stroke="currentColor" fill="none"/><circle cx="6" cy="6" r="1.5" fill="currentColor"/></svg>TRAIN</div>
      <div class="tab"><svg width="12" height="12" viewBox="0 0 12 12"><path d="M1 11V6M4 11V3M7 11V7M10 11V1" stroke="currentColor" stroke-width="1.4"/></svg>HISTORY</div>
      <div class="tab"><svg width="12" height="12" viewBox="0 0 12 12"><path d="M2 2h8M2 6h8M2 10h8" stroke="currentColor" stroke-width="1.4"/></svg>DRILLS</div>
      <div class="tab tab--active"><svg width="12" height="12" viewBox="0 0 12 12"><circle cx="6" cy="6" r="2" stroke="currentColor" fill="none"/><circle cx="6" cy="6" r="5" stroke="currentColor" stroke-dasharray="2 1.5" fill="none"/></svg>SETTINGS</div>
    </nav>
  </section>

  <section class="screen screen--teal-header" aria-label="Settings screen, teal header">
    <div class="status-bar"><span>●●●○○ NetCo</span><span class="time">12:45 AM</span><span>100%</span></div>
    <header class="app-header">
      <svg class="back" width="14" height="14" viewBox="0 0 14 14"><path d="M13 7H2M6 2L1 7l5 5" stroke="currentColor" stroke-width="1.6" fill="none"/></svg>
      Settings
    </header>

    <div class="row" style="top:84px"><span class="row-label">Pistol</span>
      <div class="icon-pair">
        <span class="icon-circle icon-circle--active"><svg width="16" height="14" viewBox="0 0 16 14"><path d="M1 2h14v4H8l-1 2H5l-1 5H1l1-6H1z" fill="#fff"/></svg></span>
        <span class="icon-plain"><svg width="16" height="16" viewBox="0 0 16 16"><path d="M2 14l10-10 2 2-10 10H2z" stroke="#c9d0d6" stroke-width="1.3" fill="none"/></svg></span>
      </div></div>
    <div class="row" style="top:126px"><span class="row-label">Current Firearm</span><span class="value">R400</span></div>
    <div class="row" style="top:168px"><span class="row-label">Right Handed</span>
      <div class="icon-pair">
        <span class="icon-plain"><svg width="14" height="16" viewBox="0 0 14 16"><path d="M3 15V6M6 15V2M9 15V3M12 15V6" stroke="#7d8791" stroke-width="1.6" stroke-linecap="round"/></svg></span>
        <span class="icon-circle icon-circle--active"><svg width="14" height="16" viewBox="0 0 14 16"><path d="M3 15V6M6 15V2M9 15V3M12 15V6" stroke="#fff" stroke-width="1.6" stroke-linecap="round"/></svg></span>
      </div></div>
    <div class="row" style="top:210px"><span class="row-label">Dry Practice</span>
      <div class="icon-pair">
        <span class="icon-circle"><svg width="10" height="16" viewBox="0 0 10 16"><rect x="1" y="1" width="8" height="14" rx="4" stroke="#c9d0d6" fill="none"/></svg></span>
        <span class="icon-plain value" style="color:#4b545d;font-size:9px">DRY</span>
      </div></div>

    <div class="row" style="top:252px"><span class="row-label">Device Mount Position</span><span class="info">i</span></div>
    <div class="seg" style="top:291px"><span>Forwards</span><span class="is-selected">Backwards</span></div>
    <div class="row" style="top:345px"><span class="row-label">Device Mount Location</span><span class="info">i</span></div>
    <div class="seg" style="top:381px"><span class="is-selected">Bottom</span><span>Top</span><span>Left</span><span>Right</span></div>
    <div class="row" style="top:441px"><span class="row-label">Bullseye Mode</span><span class="info">i</span></div>
    <div class="seg" style="top:480px"><span>Off</span><span class="is-selected">On</span></div>

    <div class="action" style="top:552px"><svg width="12" height="12" viewBox="0 0 12 12"><path d="M10 4A4.5 4.5 0 0 0 2 5M2 8a4.5 4.5 0 0 0 8-1M10 1v3H7M2 11V8h3" stroke="#e9edf0" stroke-width="1.2" fill="none"/></svg>Sync Account Data</div>
    <div class="action" style="top:597px"><svg width="12" height="12" viewBox="0 0 12 12"><path d="M3 3l6 6-3 2V1l3 2-6 6" stroke="#e9edf0" stroke-width="1.2" fill="none"/></svg>Disconnect Bluetooth</div>
    <div class="action" style="top:642px"><svg width="12" height="12" viewBox="0 0 12 12"><path d="M2 11V1h8l-2 3 2 3H2" stroke="#e9edf0" stroke-width="1.2" fill="none"/></svg>Report Issue</div>

    <div class="logout">LOGOUT</div>
    <div class="sync-info"><span>Last synced: 8:56am monday 21st 2017</span><span>v2.3.0.85</span></div>

    <nav class="tab-bar">
      <div class="tab"><svg width="12" height="12" viewBox="0 0 12 12"><circle cx="6" cy="6" r="5" stroke="currentColor" fill="none"/><circle cx="6" cy="6" r="1.5" fill="currentColor"/></svg>TRAIN</div>
      <div class="tab"><svg width="12" height="12" viewBox="0 0 12 12"><path d="M1 11V6M4 11V3M7 11V7M10 11V1" stroke="currentColor" stroke-width="1.4"/></svg>HISTORY</div>
      <div class="tab"><svg width="12" height="12" viewBox="0 0 12 12"><path d="M2 2h8M2 6h8M2 10h8" stroke="currentColor" stroke-width="1.4"/></svg>DRILLS</div>
      <div class="tab tab--active"><svg width="12" height="12" viewBox="0 0 12 12"><circle cx="6" cy="6" r="2" stroke="currentColor" fill="none"/><circle cx="6" cy="6" r="5" stroke="currentColor" stroke-dasharray="2 1.5" fill="none"/></svg>SETTINGS</div>
    </nav>
  </section>

</div>
</body>
</html>
```